New small country town business wanting to expand online wants a website to do sales, post local ...

Our logo was designed through Pixel Harbor and we loved it. We would like a website designed for us. We want to be able to sell things online, manage the upkeep ourselves, have a separate page that we can advertise local businesses, a page that contains local information and events, local Buy, sell or swap page, promote tourism in our local area, chat with us. We use LedgerLeaf and Tillpoint We also have a local business Tallowind Creek Cruises - see our website for that www.tallowindcreekcruises.com.au which we promote through our shop 'The Reel Hut'. The Reel Hut sells, hot pies, fishing tackle, bait, groceries, boating accessories, souvenir T-Shirts (also designed by Pixel Harbor) etc. Do you set it up? Do I need to get the hosting done? I dont understand what coding the website means. I apologise for my ignorance. We sell coffee and newspapers to the locals. Provide a meeting place in a town where the only other shop here actively discourages and often verbally abuses the locals.Maree
I apologise for the delay, my father is in hospital and is gravely ill. I have had to fly to Perth to be with him . Can I please have a 2 week extension? Thank you. Mar ee

```html
<!DOCTYPE html>
<html lang="en">
<head>
<meta charset="utf-8">
<title>The Reel Hut</title>
<link href="https://fonts.googleapis.com/css2?family=Lato:wght@400;700;900&display=swap" rel="stylesheet">
<style>
:root{
  --navy:#211a5f;
  --navy-deep:#1a1450;
  --red:#b3101e;
  --ink:#222;
  --grey:#6a6a6a;
  --gold:#f0a000;
  --green:#1fb53a;
  --white:#fff;
}
*{box-sizing:border-box;margin:0;padding:0}
html,body{width:1200px;height:4717px;overflow:hidden;background:var(--white)}
body{font-family:'Lato',sans-serif;color:var(--ink)}
.page{position:relative;width:1200px;height:4717px;overflow:hidden}
.abs{position:absolute}

/* header */
.topbar{left:0;top:0;width:1200px;height:40px;background:#2c2c33}
.nav{left:0;top:40px;width:1200px;height:63px;background:var(--white);z-index:3}
.nav a{position:absolute;top:24px;font-size:15px;font-weight:700;color:var(--navy);text-decoration:none;letter-spacing:.2px}
.nav a.active{color:var(--red)}
.brand-badge{left:521px;top:3px;width:158px;height:158px;border-radius:50%;background:var(--white);z-index:4;display:flex;align-items:center;justify-content:center;box-shadow:0 2px 6px rgba(0,0,0,.15)}
.brand-badge span{font-size:21px;font-weight:900;color:var(--navy);white-space:nowrap}
.cart{left:1082px;top:58px;z-index:4}

/* hero */
.hero{left:0;top:40px;width:1200px;height:684px;background:linear-gradient(180deg,#7d8187 0%,#9ea3a6 25%,#4d5b45 45%,#3f4d3a 58%,#6e2b2b 68%,#8a8f93 80%,#b7bbbf 100%)}
.hero-title{left:0;top:335px;width:1200px;text-align:center;font-size:54px;font-weight:700;color:var(--white);text-shadow:0 2px 6px rgba(0,0,0,.4);z-index:2}
.hero-sub{left:340px;top:456px;font-size:26px;font-weight:700;color:var(--white);z-index:2;white-space:nowrap}
.btn-light{left:508px;top:454px;width:182px;height:52px;border-radius:26px;background:var(--white);color:var(--navy);font-size:19px;display:flex;align-items:center;justify-content:center;gap:14px;z-index:2}
.hero-arrow{top:368px;z-index:2}
.torn{left:0;top:660px;z-index:2}

/* welcome */
.sec-title{font-size:35px;font-weight:700;color:#555}
.sec-title b{color:var(--navy)}
.rule{display:flex;gap:8px}
.rule i{display:block;height:4px;width:74px}
.welcome-title{left:108px;top:860px}
.welcome-rule{left:108px;top:922px}
.welcome-text{left:112px;top:978px;width:556px;font-size:14.5px;line-height:30px;text-align:justify;color:var(--ink)}
.btn-navy{left:108px;top:1186px;width:181px;height:54px;border-radius:27px;background:var(--navy);color:var(--white);font-size:18px;display:flex;align-items:center;justify-content:center;gap:16px}
.big-mark{left:690px;top:820px;width:420px;height:420px;display:flex;align-items:center;justify-content:center;gap:20px}
.big-mark .dot{width:64px;height:64px;border-radius:50%;background:var(--red);flex:none}
.big-mark span{font-size:46px;font-weight:900;color:var(--red);white-space:nowrap}

/* navy bands */
.band{left:0;width:1200px;background:var(--navy)}
.band-title{left:0;width:1200px;text-align:center;font-size:34px;font-weight:700;color:var(--white)}
.band-rule{justify-content:center;left:0;width:1200px}

/* tourism */
.tour-img{top:1577px;width:305px;height:217px}
.tour-cap{top:1822px;width:290px;font-size:18px;font-weight:700;color:var(--white);white-space:nowrap}
.tour-text{top:1864px;width:272px;font-size:13.5px;line-height:21px;text-align:justify;color:var(--white)}

/* products */
.prod-title{left:0;top:2097px;width:1200px;text-align:center;font-size:35px;font-weight:700;color:#6a6a6a}
.prod-intro{left:150px;top:2201px;width:900px;text-align:center;font-size:14.5px;line-height:30px;color:var(--ink)}
.card{top:2336px;width:224px;height:265px;background:var(--white);border:2px solid #c9c9c9}
.card.lift{border:none;box-shadow:0 0 40px rgba(0,0,0,.18)}
.card .ico{position:absolute;left:14px}
.card .pic{position:absolute;left:38px;top:26px;width:150px;height:210px;border-radius:4px}
.prod-name{top:2646px;width:224px;text-align:center;font-size:22px;font-weight:700;color:#707070;white-space:nowrap}
.stars{top:2690px;width:224px;text-align:center;font-size:15px;letter-spacing:3px;color:var(--gold)}
.dots{display:flex;gap:12px;justify-content:center;left:0;width:1200px}
.dots i{width:14px;height:14px;border-radius:50%;display:block}

/* gallery */
.gal{position:absolute}

/* events */
.events-title{left:0;top:3718px;width:1200px;text-align:center;font-size:38px;font-weight:700;color:var(--ink)}
.ev{top:3825px;width:475px;height:284px;background:var(--white);box-shadow:0 4px 18px rgba(0,0,0,.14)}
.ev .pic{position:absolute;left:0;top:0;width:172px;height:284px}
.ev h3{position:absolute;left:204px;top:36px;font-size:19px;font-weight:700;color:var(--ink);letter-spacing:-.3px;white-space:nowrap}
.ev .date{position:absolute;left:204px;top:72px;font-size:12px;color:var(--ink)}
.ev .line{position:absolute;left:204px;top:102px;width:60px;height:2px;background:var(--red)}
.ev p{position:absolute;left:204px;top:124px;width:250px;font-size:12.5px;line-height:24px;color:#444}
.ev .meta{position:absolute;left:204px;top:228px;font-size:11px;color:#444;display:flex;align-items:center;gap:10px}
.ev .user{position:absolute;left:425px;top:224px}
.chat{left:920px;top:4155px;width:170px;height:66px;background:var(--green);color:var(--white);font-size:18px;font-weight:700;display:flex;align-items:center;justify-content:center;gap:10px;white-space:nowrap}

/* footer */
.footer{left:0;top:4268px;width:1200px;height:396px;background:var(--navy)}
.foot-brand{left:112px;top:4360px;display:flex;align-items:center;gap:16px}
.foot-brand .dot{width:40px;height:40px;border-radius:50%;border:3px solid var(--white)}
.foot-brand span{font-size:38px;font-weight:700;color:var(--white);white-space:nowrap}
.foot-blurb{left:130px;top:4527px;width:310px;font-size:15px;line-height:26px;color:var(--white)}
.contact{left:522px;display:flex;gap:22px;font-size:17px;line-height:28px;color:var(--white)}
.social{left:872px;display:flex;align-items:center;gap:24px;font-size:18px;color:var(--white)}
.pay{top:4592px;font-size:24px;color:var(--white);white-space:nowrap}
.bottom{left:0;top:4664px;width:1200px;height:53px;background:#121212;color:var(--white);font-size:13px;padding:20px 0 0 112px}
</style>
</head>
<body>
<div class="page">

  <!-- header -->
  <div class="abs topbar"></div>
  <nav class="abs nav">
    <a class="active" style="left:183px">HOME</a>
    <a style="left:280px">ABOUT US</a>
    <a style="left:405px">PRODUCTS</a>
    <a style="left:706px">SERVICES</a>
    <a style="left:830px">TOURISM</a>
    <a style="left:958px">CONTACT US</a>
  </nav>
  <div class="abs brand-badge"><span>The Reel Hut</span></div>
  <svg class="abs cart" width="44" height="36" viewBox="0 0 44 36" fill="none" stroke="#211a5f" stroke-width="2.4">
    <path d="M2 4h6l5 20h22l4-14H11"/><circle cx="16" cy="31" r="3"/><circle cx="32" cy="31" r="3"/>
    <circle cx="34" cy="18" r="7" fill="#fff"/><path d="M34 14v8M30 18h8"/>
  </svg>

  <!-- hero -->
  <div class="abs hero" role="img" aria-label="Photo of a red boat shed on a mountain lake with kayaks along the jetty"></div>
  <h1 class="abs hero-title">Welcome Reel Hut</h1>
  <div class="abs hero-sub">Reel Hut</div>
  <div class="abs btn-light">Get started
    <svg width="26" height="20" viewBox="0 0 26 20"><path d="M0 0l26 10L0 20l6-10z" fill="#211a5f"/></svg>
  </div>
  <svg class="abs hero-arrow" style="left:112px" width="50" height="50" viewBox="0 0 50 50" fill="none" stroke="#b3101e" stroke-width="3">
    <circle cx="25" cy="25" r="22"/><path d="M36 25H15M23 16l-9 9 9 9"/>
  </svg>
  <svg class="abs hero-arrow" style="left:1038px" width="50" height="50" viewBox="0 0 50 50" fill="none" stroke="#b3101e" stroke-width="3">
    <circle cx="25" cy="25" r="22"/><path d="M14 25h21M27 16l9 9-9 9"/>
  </svg>
  <svg class="abs torn" width="1200" height="70" viewBox="0 0 1200 70" preserveAspectRatio="none">
    <path d="M0 30 L60 42 L120 26 L190 46 L260 30 L330 50 L400 34 L470 48 L540 28 L610 44 L690 30 L760 48 L830 32 L900 46 L980 28 L1050 44 L1120 30 L1200 40 L1200 70 L0 70Z" fill="#fff"/>
  </svg>

  <!-- welcome -->
  <h2 class="abs sec-title welcome-title">Welcome To <b>Reel Hut</b></h2>
  <div class="abs rule welcome-rule"><i style="background:#555"></i><i style="background:var(--navy)"></i></div>
  <p class="abs welcome-text">Lorem ipsum dolor sit amet, consectetur adipiscing elit, sed do eiusmod tempor incididunt ut labore et dolore magna aliqua. Quis ipsum suspendisse ultrices gravida. Risus commodo viverra maecenas accumsan lacus vel facilisis. Lorem ipsum dolor sit amet, consectetur adipiscing elit, sed do eiusmod tempor incididunt ut labore et dolore magna aliqua. Quis ipsum suspendisse ultrices gravida. Risus commodo viverra maecenas accumsan lacus vel facilisis.</p>
  <div class="abs btn-navy">Read More
    <svg width="24" height="18" viewBox="0 0 26 20"><path d="M0 0l26 10L0 20l6-10z" fill="#fff"/></svg>
  </div>
  <div class="abs big-mark"><div class="dot"></div><span>The Reel Hut</span></div>

  <!-- tourism -->
  <section class="abs band" style="top:1310px;height:727px"></section>
  <h2 class="abs band-title" style="top:1392px">Tourism in our local area</h2>
  <div class="abs rule band-rule" style="top:1456px"><i style="background:var(--red)"></i><i style="background:#fff"></i></div>

  <div class="abs tour-img" style="left:112px;background:linear-gradient(180deg,#2f6fc4 0%,#6a9ad6 35%,#a3322c 55%,#7a2621 75%,#4a3a2e 100%)" role="img" aria-label="Photo of a red fishing shack on a harbour wharf"></div>
  <div class="abs tour-img" style="left:447px;background:linear-gradient(180deg,#3c3d77 0%,#b5648c 40%,#e9884a 55%,#2a2c3e 80%,#1f2033 100%)" role="img" aria-label="Photo of a harbour bridge at sunset"></div>
  <div class="abs tour-img" style="left:782px;background:linear-gradient(180deg,#8fc0e6 0%,#cfe3f0 25%,#2a8fa3 45%,#4f7d3a 70%,#3a5a28 100%)" role="img" aria-label="Photo of walkers on a coastal track above a beach"></div>

  <h3 class="abs tour-cap" style="left:134px">Lorem ipsum dolor sit amet,</h3>
  <h3 class="abs tour-cap" style="left:480px">Lorem ipsum dolor sit amet,</h3>
  <h3 class="abs tour-cap" style="left:816px">Lorem ipsum dolor sit amet,</h3>
  <p class="abs tour-text" style="left:134px">Lorem ipsum dolor sit amet, consectetur adipiscing elit, sed do eiusmod tempor incididunt ut labore et dolore magna aliqua.</p>
  <p class="abs tour-text" style="left:477px">Lorem ipsum dolor sit amet, consectetur adipiscing elit, sed do eiusmod tempor incididunt ut labore et dolore magna aliqua.</p>
  <p class="abs tour-text" style="left:816px">Lorem ipsum dolor sit amet, consectetur adipiscing elit, sed do eiusmod tempor incididunt ut labore et dolore magna aliqua.</p>

  <!-- products -->
  <h2 class="abs prod-title">Products</h2>
  <div class="abs rule band-rule" style="top:2160px"><i style="background:#6a6a6a"></i><i style="background:var(--navy)"></i></div>
  <p class="abs prod-intro">Lorem ipsum dolor sit amet, consectetur adipiscing elit, sed do eiusmod tempor incididunt ut labore et dolore magna aliqua. Quis ipsum suspendisse ultrices gravida. Risus commodo viverra maecenas accumsan lacus vel facilisis. Lorem ipsum dolor sit amet,</p>

  <div class="abs card" style="left:117px">
    <svg class="ico" style="top:20px" width="20" height="12" viewBox="0 0 20 12"><path d="M1 6c4-7 14-7 18 0-4 7-14 7-18 0z" fill="none" stroke="#b3101e" stroke-width="2"/><circle cx="10" cy="6" r="3" fill="#b3101e"/></svg>
    <svg class="ico" style="top:44px" width="20" height="18" viewBox="0 0 20 18"><path d="M10 17L2 9a5 5 0 018-6 5 5 0 018 6z" fill="#b3101e"/></svg>
    <div class="pic" style="background:radial-gradient(circle at 50% 50%,#8a6a4a 0%,#d9d2ca 35%,#fff 70%)" role="img" aria-label="Photo of a fishing rod and reel"></div>
  </div>
  <div class="abs card lift" style="left:372px">
    <svg class="ico" style="top:20px" width="20" height="12" viewBox="0 0 20 12"><path d="M1 6c4-7 14-7 18 0-4 7-14 7-18 0z" fill="none" stroke="#b3101e" stroke-width="2"/><circle cx="10" cy="6" r="3" fill="#b3101e"/></svg>
    <svg class="ico" style="top:44px" width="20" height="18" viewBox="0 0 20 18"><path d="M10 17L2 9a5 5 0 018-6 5 5 0 018 6z" fill="#b3101e"/></svg>
    <div class="pic" style="background:radial-gradient(circle at 50% 45%,#111 0%,#222 38%,#fff 62%)" role="img" aria-label="Photo of a black souvenir T-shirt"></div>
  </div>
  <div class="abs card" style="left:623px">
    <svg class="ico" style="top:20px" width="20" height="12" viewBox="0 0 20 12"><path d="M1 6c4-7 14-7 18 0-4 7-14 7-18 0z" fill="none" stroke="#b3101e" stroke-width="2"/><circle cx="10" cy="6" r="3" fill="#b3101e"/></svg>
    <svg class="ico" style="top:44px" width="20" height="18" viewBox="0 0 20 18"><path d="M10 17L2 9a5 5 0 018-6 5 5 0 018 6z" fill="#b3101e"/></svg>
    <div class="pic" style="background:radial-gradient(circle at 50% 45%,#b8b833 0%,#7a8a3a 25%,#fff 55%)" role="img" aria-label="Photo of a fishing lure"></div>
  </div>
  <div class="abs card" style="left:874px">
    <svg class="ico" style="top:20px" width="20" height="12" viewBox="0 0 20 12"><path d="M1 6c4-7 14-7 18 0-4 7-14 7-18 0z" fill="none" stroke="#b3101e" stroke-width="2"/><circle cx="10" cy="6" r="3" fill="#b3101e"/></svg>
    <svg class="ico" style="top:44px" width="20" height="18" viewBox="0 0 20 18"><path d="M10 17L2 9a5 5 0 018-6 5 5 0 018 6z" fill="#b3101e"/></svg>
    <div class="pic" style="background:radial-gradient(circle at 50% 55%,#b08050 0%,#6a9a3a 35%,#fff 65%)" role="img" aria-label="Photo of a paper bag of groceries and vegetables"></div>
  </div>

  <div class="abs prod-name" style="left:117px">Fishing tackle</div>
  <div class="abs prod-name" style="left:372px">Souvenir T-Shirts</div>
  <div class="abs prod-name" style="left:623px">Bait</div>
  <div class="abs prod-name" style="left:874px">Groceries</div>
  <div class="abs stars" style="left:117px">★★★★★</div>
  <div class="abs stars" style="left:372px">★★★★★</div>
  <div class="abs stars" style="left:623px">★★★★★</div>
  <div class="abs stars" style="left:874px">★★★★★</div>
  <div class="abs dots" style="top:2761px"><i style="background:var(--navy)"></i><i style="background:var(--navy)"></i><i style="background:var(--navy)"></i></div>

  <!-- gallery -->
  <section class="abs band" style="top:2830px;height:821px"></section>
  <h2 class="abs band-title" style="top:2915px;left:-22px">Gallery</h2>
  <div class="abs rule band-rule" style="top:2976px;left:0"><i style="background:#888"></i><i style="background:#fff"></i></div>

  <div class="gal" style="left:112px;top:3047px;width:392px;height:247px;background:linear-gradient(135deg,#e8e4dc 0%,#f4f2ee 45%,#c9b28a 100%)" role="img" aria-label="Photo of a branded coffee mug on a counter"></div>
  <div class="gal" style="left:514px;top:3047px;width:327px;height:247px;background:linear-gradient(180deg,#9bb4cc 0%,#b3c4d2 30%,#a3303a 50%,#5a6a7a 75%,#3a4a5a 100%)" role="img" aria-label="Photo of red waterfront houses and a boat at a jetty"></div>
  <div class="gal" style="left:851px;top:3047px;width:245px;height:474px;background:linear-gradient(180deg,#d8d8d8 0%,#9a9a9a 40%,#555 70%,#2a2a2a 100%)" role="img" aria-label="Photo of a stack of takeaway coffee cups"></div>
  <div class="gal" style="left:112px;top:3307px;width:237px;height:214px;background:linear-gradient(180deg,#6b8fc0 0%,#a63438 45%,#4a6a8a 70%,#6e6a5e 100%)" role="img" aria-label="Photo of a red boat shed by the sea"></div>
  <div class="gal" style="left:357px;top:3307px;width:237px;height:214px;background:linear-gradient(135deg,#3a4a4a 0%,#7a8a8a 50%,#2a3030 100%)" role="img" aria-label="Photo of hands holding a fishing reel"></div>
  <div class="gal" style="left:604px;top:3307px;width:237px;height:214px;background:linear-gradient(180deg,#cfe0ef 0%,#4a7fb8 40%,#2d5d94 70%,#8a6a4a 100%)" role="img" aria-label="Photo of a cup of coffee on a jetty rail above the water"></div>

  <div class="abs dots" style="top:3597px"><i style="background:#fff"></i><i style="background:#fff"></i><i style="background:#fff"></i></div>

  <!-- events -->
  <h2 class="abs events-title">Events</h2>

  <article class="abs ev" style="left:112px">
    <div class="pic" style="background:linear-gradient(180deg,#6a7f9a 0%,#8a8a8a 35%,#8a4a32 65%,#6a3a2a 100%)" role="img" aria-label="Photo of a waterfront street lit by lamps"></div>
    <h3>Lorem ipsum is best</h3>
    <div class="date">on Aug 13, 2019 9:58 AM</div>
    <div class="line"></div>
    <p>Lorem ipsum dolor sit amet, consectetur adipiscing elit, sed do eiusmod tempor incididunt ut labore et dolore magna</p>
    <div class="meta"><svg width="13" height="13" viewBox="0 0 13 13" fill="none" stroke="#555"><rect x="1" y="1" width="11" height="9"/><path d="M3 4h7M3 7h5"/></svg>24 comments</div>
    <svg class="user" width="28" height="28" viewBox="0 0 28 28"><rect width="28" height="28" rx="3" fill="#b3101e"/><circle cx="14" cy="11" r="5" fill="none" stroke="#fff" stroke-width="2"/><path d="M6 23c2-5 14-5 16 0" fill="none" stroke="#fff" stroke-width="2"/></svg>
  </article>
  <article class="abs ev" style="left:617px">
    <div class="pic" style="background:linear-gradient(180deg,#d9a36a 0%,#c47a4a 40%,#8a3a3a 70%,#4a2a3a 100%)" role="img" aria-label="Photo of people enjoying drinks at a summer gathering"></div>
    <h3>Lorem ipsum is best</h3>
    <div class="date">on Aug 13, 2019 9:58 AM</div>
    <div class="line"></div>
    <p>Lorem ipsum dolor sit amet, consectetur adipiscing elit, sed do eiusmod tempor incididunt ut labore et dolore magna</p>
    <div class="meta"><svg width="13" height="13" viewBox="0 0 13 13" fill="none" stroke="#555"><rect x="1" y="1" width="11" height="9"/><path d="M3 4h7M3 7h5"/></svg>24 comments</div>
    <svg class="user" width="28" height="28" viewBox="0 0 28 28"><rect width="28" height="28" rx="3" fill="#b3101e"/><circle cx="14" cy="11" r="5" fill="none" stroke="#fff" stroke-width="2"/><path d="M6 23c2-5 14-5 16 0" fill="none" stroke="#fff" stroke-width="2"/></svg>
  </article>

  <div class="abs chat">
    <svg width="30" height="24" viewBox="0 0 30 24" fill="none" stroke="#fff" stroke-width="2"><path d="M3 11a9 7 0 1118 0 9 7 0 01-13 6l-5 2 2-4a7 7 0 01-2-4z"/><path d="M22 8a7 6 0 015 10l1 4-4-2a8 6 0 01-7-1"/></svg>
    Chat with us
  </div>

  <!-- footer -->
  <footer class="abs footer"></footer>
  <svg class="abs" style="left:0;top:4252px" width="1200" height="40" viewBox="0 0 1200 40" preserveAspectRatio="none">
    <path d="M0 22 L70 12 L140 26 L220 10 L300 24 L380 14 L460 28 L540 12 L620 26 L700 10 L780 24 L860 14 L940 28 L1020 12 L1100 24 L1200 16 L1200 40 L0 40Z" fill="#211a5f"/>
  </svg>
  <div class="abs foot-brand"><div class="dot"></div><span>The Reel Hut</span></div>
  <p class="abs foot-blurb">Lorem ipsum dolor sit amet, consectetur adipiscing elit, sed do eiusmod tempor</p>

  <div class="abs contact" style="top:4343px">
    <svg width="20" height="20" viewBox="0 0 20 20" style="margin-top:5px"><path d="M19 1L1 9l7 3 3 7z" fill="#fff"/></svg>
    <span>112 Quarry Bend Road<br>Larkvale, New South<br>Wales 2790</span>
  </div>
  <div class="abs contact" style="top:4454px">
    <svg width="20" height="20" viewBox="0 0 20 20" style="margin-top:4px"><path d="M4 1l4 4-2 3c1 3 3 5 6 6l3-2 4 4-3 3C8 19 1 12 1 4z" fill="#fff"/></svg>
    <span>61 2 5550 1827</span>
  </div>
  <div class="abs contact" style="top:4511px">
    <svg width="20" height="16" viewBox="0 0 20 16" style="margin-top:6px"><rect width="20" height="16" rx="1" fill="#fff"/><path d="M1 1l9 8 9-8" fill="none" stroke="#211a5f" stroke-width="2"/></svg>
    <span>info@reelhut.com</span>
  </div>

  <div class="abs social" style="top:4344px"><svg width="16" height="16"><rect width="16" height="16" fill="#fff"/></svg>Shorelink</div>
  <div class="abs social" style="top:4390px"><svg width="16" height="16"><rect width="16" height="16" fill="#fff"/></svg>Chirper</div>
  <div class="abs social" style="top:4438px"><svg width="16" height="16"><circle cx="8" cy="8" r="7" fill="#fff"/></svg>Snapgram</div>
  <div class="abs social" style="top:4484px"><svg width="16" height="16"><rect width="16" height="16" fill="#fff"/></svg>ViewTube</div>

  <div class="abs pay" style="left:820px">Tillpoint</div>
  <div class="abs pay" style="left:940px">LedgerLeaf</div>

  <div class="abs bottom">Copyrights 2019. All rights reserved</div>
</div>
</body>
</html>
```